business card with logo

Would like a business card for an electrical contractor called BRANLOCK ELECTRICS.
No generic electrical imagery (light globe, powerpoints, ect). Would like a logo or symbol created in the design as part of the project . I would like crisp colour. No templated designs like Printvox

is there any other designers willing to submit designs

Electrical

```html
<!DOCTYPE html>
<html lang="en">
<head>
<meta charset="utf-8">
<title>Branlock Electrics – Business Card</title>
<link rel="stylesheet" href="https://fonts.googleapis.com/css2?family=Arimo:wght@400&family=Roboto+Condensed:wght@300;400&display=swap">
<style>
  :root {
    --page: #ffffff;
    --card: #000000;
    --brand-front: #bdbdbd;
    --brand-back: #5a5a5a;
    --name: #d6d6d6;
    --title: #bdbdbd;
    --detail: #8a8a8a;
    --url: #8c8c8c;
  }
  html, body {
    margin: 0;
    padding: 0;
    width: 1200px;
    height: 1200px;
    overflow: hidden;
    background: var(--page);
  }
  .canvas {
    position: relative;
    width: 1200px;
    height: 1200px;
  }
  .card {
    position: absolute;
    left: 402px;
    width: 392px;
    height: 224px;
    background: var(--card);
    box-shadow: 5px 6px 8px rgba(0,0,0,0.28);
  }
  .card--front { top: 278px; }
  .card--back { top: 578px; }

  .brand-name {
    position: absolute;
    margin: 0;
    font-family: "Arimo", Arial, sans-serif;
    font-weight: 400;
    line-height: 1;
    white-space: nowrap;
  }
  .card--front .brand-name {
    right: 26px;
    top: 34px;
    font-size: 13px;
    color: var(--brand-front);
  }
  .card--back .brand-name {
    left: 0;
    right: 0;
    top: 76px;
    text-align: center;
    font-size: 22px;
    color: var(--brand-back);
  }

  .contact-name {
    position: absolute;
    left: 23px;
    top: 88px;
    margin: 0;
    font-family: "Roboto Condensed", "Arial Narrow", sans-serif;
    font-weight: 300;
    font-size: 21px;
    color: var(--name);
    line-height: 1;
  }
  .contact-role {
    position: absolute;
    left: 23px;
    top: 114px;
    margin: 0;
    font-family: "Arimo", Arial, sans-serif;
    font-size: 12.5px;
    color: var(--title);
    line-height: 1;
  }
  .contact-details {
    position: absolute;
    left: 23px;
    top: 150px;
    margin: 0;
    padding: 0;
    list-style: none;
    font-family: "Arimo", Arial, sans-serif;
    font-size: 10px;
    letter-spacing: 0.4px;
    line-height: 12px;
    color: var(--detail);
  }
  .website {
    position: absolute;
    left: 0;
    right: 0;
    top: 188px;
    margin: 0;
    text-align: center;
    font-family: "Arimo", Arial, sans-serif;
    font-size: 15px;
    letter-spacing: 1.6px;
    color: var(--url);
  }
</style>
</head>
<body>
<main class="canvas">
  <section class="card card--front" aria-label="Business card front">
    <p class="brand-name">BRANLOCK ELECTRICS</p>
    <h1 class="contact-name">Megan Harlow</h1>
    <p class="contact-role">Parts Manager</p>
    <ul class="contact-details">
      <li>Phone: (07) 4000 1234</li>
      <li>Fax: (07) 4000 1290</li>
      <li>Email: parts@branlock.com.au</li>
      <li>Address: 14 Carrow Street (PO Box 1180) Ridgeview QLD 4800</li>
    </ul>
  </section>

  <section class="card card--back" aria-label="Business card back">
    <p class="brand-name">BRANLOCK ELECTRICS</p>
    <p class="website">www.branlock.com.au</p>
  </section>
</main>
</body>
</html>
```